Landing page for buying gold and stamps

Create a landing page for our purchase. We buy postage stamps, franked goods, gold coins, scrap gold, silver money, etc. We don't want to sell anything to people, we just shop. So the visitors should send their old gold, their stamps, etc. by post. We then estimate the value and transfer the money by bank or you can collect it in cash.

The visitor should see what he can sell. If he fills in his contact details, he will receive our purchase form and the mailing label by post so that he can send in his sales goods free of charge. Or he can call us or write an e-mail and come to us directly.

We buy:
When the form is filled out, an email will be sent to our address with the following data:
Surname
First name
Street, Nr.
Post loan number
place
What do you want to sell

In the appendix I have added designs of flyers. You can see what we buy on it. What is missing on the flyer, however, are stamps, franking goods and rarities. In addition, the design should be similar. The logo can also be used.

In addition, the following text should be on the page:
Do you need help selling an inherited collection? Feel free to contact us. We are happy to help. We have been in the stamp and coin trade for nearly 100 years.

I have also attached a picture of the stamp as an attachment. This should also be put on the side with old gold and gold coins.

And here you will find our current purchase pages:
https://www.briefhaus-tanner.ch/ankauf-gold-und-silber
https://www.briefhaus-tanner.ch/ankauf-frankatur

Competitors' pages:
https://www.edelwertplatz.ch/goldankauf/
https://www.talerbruhin.ch/ankauf-1/altgold-ankauf1.html?gclid=Xq7RtLwPzN2vKdFaYbHsUmEcGjTnQoVrZiBxWkLpDyAsCfNhMuJbOeTgIlKwSvHaRdYqPzXnBmCtGuFoLiEkJrQsWvTy

Target Market(s)

Private persons

Font styles to use
Serif
Sans Serif

Requirements
Must have
• It must be clear that anyone who wants to sell their gold, stamps or coins can do so easily from home by post. You no longer have to go to a store.
Steps to Sell:
1. You fill out your contact details
2. We will send you a form and a label for shipping (no postage for you!)
3. You will receive a non-binding purchase offer
4. You will receive the money transferred or you can collect it in cash (or we will send you the valuables you have sent back)

You have no costs! Simply sell your gold or stamps from home.

```html
<!DOCTYPE html>
<html lang="en">
<head>
<meta charset="utf-8">
<title>Briefhaus Tanner – Sell gold and stamps from home</title>
<link href="https://fonts.googleapis.com/css2?family=Noto+Serif:ital,wght@0,400;1,400;1,700&family=Lato:wght@400;700&family=Raleway:wght@500;600;700&display=swap" rel="stylesheet">
<style>
:root{
  --blue:#2e3192;
  --blue-dark:#272a7e;
  --red:#e84c3d;
  --ink:#333;
  --muted:#666;
  --grey-bg:#ececec;
  --line:#e8e8e8;
  --white:#fff;
  --serif:"Noto Serif", Georgia, serif;
  --sans:"Lato", Arial, sans-serif;
  --display:"Raleway", Arial, sans-serif;
}
*{box-sizing:border-box;margin:0;padding:0}
html,body{width:1200px;height:2786px;overflow:hidden}
body{position:relative;background:var(--white);font-family:var(--sans);color:var(--ink)}
.abs{position:absolute}

/* top bar */
.topbar{left:0;top:0;width:1200px;height:35px;border:1px solid var(--line);font-size:10.5px}
.topbar .contact{left:172px;top:11px;color:#444}
.topbar .contact b{font-weight:700}
.topbar .menu{top:11px;color:#444}

/* header */
.header{left:0;top:35px;width:1200px;height:81px;background:var(--white)}
.brand{left:173px;top:27px;display:flex;align-items:center;gap:8px}
.brand-mark{width:22px;height:22px;background:var(--red)}
.brand-name{font-family:var(--sans);font-weight:700;font-size:19px;color:var(--blue);letter-spacing:.5px}
.nav{top:38px;font-family:var(--display);font-weight:600;font-size:11.5px;letter-spacing:1px;color:#444}

/* hero */
.hero{left:0;top:116px;width:1200px;height:484px;background:radial-gradient(ellipse at 50% 40%,#fafafa 0%,#eaeaea 70%,#e2e2e2 100%)}
.hero-title{left:0;top:170px;width:1200px;text-align:center;font-family:var(--serif);font-style:italic;font-size:36px;line-height:48px;color:#333;text-transform:uppercase}
.hero-visual{left:146px;top:254px;width:617px;height:346px;background:radial-gradient(ellipse at 25% 40%,#d6574a 0%,#c9b9a2 28%,transparent 45%),radial-gradient(ellipse at 62% 55%,#d9a53a 0%,#c98f2a 35%,#b8862f 50%,transparent 70%);}
.help-band{left:0;top:600px;width:1200px;height:115px;background:var(--red)}
.help-text{left:171px;top:629px;font-family:var(--display);font-weight:700;font-size:20px;line-height:25px;color:var(--white);letter-spacing:.6px}
.help-text svg{vertical-align:-3px;margin-left:8px}

/* sell form */
.sell-form{left:770px;top:329px;width:258px;height:387px;background:var(--blue);padding:18px 23px 0}
.sell-form h2{font-family:var(--display);font-weight:600;font-size:21px;color:var(--white);text-align:center;margin-bottom:12px}
.field{display:block;width:212px;height:32px;background:var(--white);border:1px solid #ddd;margin-bottom:13px;padding:0 12px;font-family:var(--display);font-weight:500;font-size:13.5px;line-height:31px;color:#aaa;letter-spacing:.4px}
.send-btn{display:block;width:212px;height:32px;background:#333;border:1px solid #222;color:var(--white);font-family:var(--display);font-weight:700;font-size:12.5px;text-align:center;line-height:31px;letter-spacing:.6px;margin-top:2px}

/* section heads */
.section-title{left:0;width:1200px;text-align:center;font-family:var(--serif);font-style:italic;font-weight:700;font-size:24px;color:#333;text-transform:uppercase}
.section-sub{left:0;width:1200px;text-align:center;font-family:var(--serif);font-size:18.5px;color:#444}

/* goods */
.good{width:265px}
.good h3{font-family:var(--display);font-weight:700;font-size:13.5px;letter-spacing:.6px;color:#333;margin-bottom:14px}
.good p{font-size:12.2px;line-height:19px;color:var(--muted)}

/* channels */
.channel{top:1343px;width:400px;height:270px;padding:0 45px;color:var(--white)}
.channel.blue{background:var(--blue)}
.channel.red{background:var(--red)}
.channel h3{margin-top:54px;font-family:var(--serif);font-style:italic;font-weight:700;font-size:19px;text-transform:uppercase}
.channel p{margin-top:24px;font-size:12.2px;line-height:19px}
.channel .call{margin-top:38px;font-family:var(--serif);font-style:italic;font-weight:700;font-size:22px}
.channel .btn{display:inline-block;margin-top:38px;border:2px solid var(--white);padding:0 14px;height:36px;line-height:32px;font-family:var(--display);font-weight:700;font-size:11.5px;letter-spacing:.6px}

/* steps */
.step{width:412px}
.step h3{font-family:var(--display);font-weight:500;font-size:14.5px;color:#333;line-height:17px}
.step p{margin-top:14px;font-size:12.2px;line-height:19px;color:var(--muted)}
.rule{height:1px;background:var(--line)}

/* heritage */
.heritage{left:0;top:2281px;width:1200px;height:252px;background:radial-gradient(ellipse at 30% 70%,#4a3a22 0%,#2f2b26 45%,#2a2a2a 100%)}
.heritage-text{left:0;top:2363px;width:1200px;text-align:center;font-family:var(--serif);font-style:italic;font-size:30px;line-height:42px;color:var(--white);text-transform:uppercase}

/* footer */
.footer{left:0;top:2537px;width:1200px;height:179px;background:var(--blue);border-top:4px solid var(--white)}
.foot-col{top:2581px;color:#d8d9f0}
.foot-col h4{font-family:var(--display);font-weight:600;font-size:12.5px;letter-spacing:1px;color:#e6e7f6;margin-bottom:22px}
.foot-col li{list-style:none;font-family:var(--display);font-size:10.5px;margin-bottom:9px;letter-spacing:.3px}
.foot-col li::before{content:"›";margin-right:9px}
.foot-call{left:813px;top:2578px;font-family:var(--serif);font-size:21px;color:var(--white)}
.foot-mail{left:813px;top:2611px;font-family:var(--display);font-weight:600;font-size:10.5px;letter-spacing:1px;color:#e6e7f6}
.social{left:811px;top:2641px;display:flex;align-items:center;gap:8px;color:var(--white);font-size:8px;line-height:12px}
.social .square{width:28px;height:28px;background:#3c3fa6}
.bottom-bar{left:0;top:2716px;width:1200px;height:70px;background:var(--blue-dark);padding:18px 0 0 172px;font-size:10px;line-height:21px;color:#7d80c4}
</style>
</head>
<body>

<div class="abs topbar">
  <span class="abs contact"><b>Call:</b> 0800-000-0000 | <b>Email:</b> info@briefhaus-tanner.ch</span>
  <span class="abs menu" style="left:788px">Menu1</span>
  <span class="abs menu" style="left:853px">Menu2</span>
  <span class="abs menu" style="left:918px">Menu3</span>
  <span class="abs menu" style="left:984px">Menu4</span>
</div>

<header class="abs header">
  <div class="abs brand"><span class="brand-mark"></span><span class="brand-name">BRIEFHAUS TANNER</span></div>
  <nav>
    <span class="abs nav" style="left:543px">HOME</span>
    <span class="abs nav" style="left:603px">FEATURES</span>
    <span class="abs nav" style="left:689px">PAGES</span>
    <span class="abs nav" style="left:754px">ADD MEMU</span>
    <span class="abs nav" style="left:845px">PAGES</span>
    <span class="abs nav" style="left:909px">ADD MENU</span>
    <svg class="abs" style="left:1007px;top:40px" width="11" height="11" viewBox="0 0 11 11"><circle cx="4.5" cy="4.5" r="3.3" fill="none" stroke="#444" stroke-width="1.6"/><line x1="7" y1="7" x2="10" y2="10" stroke="#444" stroke-width="1.8"/></svg>
  </nav>
</header>

<section>
  <div class="abs hero"></div>
  <h1 class="abs hero-title">You have no costs! Simply sell your gold<br>or stamps from home</h1>
  <div class="abs hero-visual" role="img" aria-label="Historic postage stamp beside a pile of gold coins and gold jewellery"></div>
  <div class="abs help-band"></div>
  <p class="abs help-text">Do you need help selling an inherited collection?<svg width="19" height="19" viewBox="0 0 19 19"><circle cx="9.5" cy="9.5" r="9" fill="#fff"/><path d="M5 9.5h8M9.5 5.5l4 4-4 4" fill="none" stroke="#e84c3d" stroke-width="2.4"/></svg><br>Feel free to contact us. We are happy to help.</p>

  <form class="abs sell-form">
    <h2>START SELLING</h2>
    <span class="field">Surname</span>
    <span class="field">First name</span>
    <span class="field">Street, Nr.</span>
    <span class="field">Post loan number</span>
    <span class="field">Place</span>
    <span class="field">What do you want to sell</span>
    <span class="send-btn">SEND</span>
  </form>
</section>

<section>
  <h2 class="abs section-title" style="top:826px">What you can sell</h2>
  <p class="abs section-sub" style="top:873px">Lorem ipsum dolor sit amet, consectetur adipiscing elit</p>

  <div class="abs good" style="left:170px;top:940px"><h3>POSTAGE STAMPS</h3><p>Duis sit amet sollicitudin ante, nonpulvinar orci. Interdum et malesuada fames ac ante ipsum primis in faucibus. Duis sit amet sollicitudin ante, nonpulvinar orci. Interdum et malesuada fames ac ante ipsum primis in faucibus.</p></div>
  <div class="abs good" style="left:470px;top:940px"><h3>FRANKED GOODS</h3><p>Duis sit amet sollicitudin ante, nonpulvinar orci. Interdum et malesuada fames ac ante ipsum primis in faucibus. Duis sit amet sollicitudin ante, nonpulvinar orci. Interdum et malesuada fames ac ante ipsum primis in faucibus.</p></div>
  <div class="abs good" style="left:770px;top:940px"><h3>GOLD COINS</h3><p>Duis sit amet sollicitudin ante, nonpulvinar orci. Interdum et malesuada fames ac ante ipsum primis in faucibus. Duis sit amet sollicitudin ante, nonpulvinar orci. Interdum et malesuada fames ac ante ipsum primis in faucibus.</p></div>
  <div class="abs good" style="left:170px;top:1111px"><h3>SCRAP GOLD</h3><p>Duis sit amet sollicitudin ante, nonpulvinar orci. Interdum et malesuada fames ac ante ipsum primis in faucibus. Duis sit amet sollicitudin ante, nonpulvinar orci. Interdum et malesuada fames ac ante ipsum primis in faucibus.</p></div>
  <div class="abs good" style="left:471px;top:1111px"><h3>SILVER MONEY</h3><p>Duis sit amet sollicitudin ante, nonpulvinar orci. Interdum et malesuada fames ac ante ipsum primis in faucibus. Duis sit amet sollicitudin ante, nonpulvinar orci. Interdum et malesuada fames ac ante ipsum primis in faucibus.</p></div>
</section>

<section>
  <div class="abs channel blue" style="left:0">
    <h3>Call us to sell</h3>
    <p>Lorem ipsum dolor sit amet, consectetur adipisicing ero quod consequuntur quibusdam, enim expedita nesciunt incidunt accusamus necessitatibus modi ad.</p>
    <div class="call">Call: 0445550000</div>
  </div>
  <div class="abs channel red" style="left:400px">
    <h3>Sell by email</h3>
    <p>Lorem ipsum dolor sit amet, consectetur adipisicing ero quod consequuntur quibusdam, enim expedita nesciunt incidunt accusamus necessitatibus modi ad.</p>
    <span class="btn">SEND MAIL</span>
  </div>
  <div class="abs channel blue" style="left:800px">
    <h3>Fill out your details</h3>
    <p>Lorem ipsum dolor sit amet, consectetur adipisicing ero quod consequuntur quibusdam, enim expedita nesciunt incidunt accusamus necessitatibus modi ad.</p>
    <span class="btn">FILL THE FORM</span>
  </div>
</section>

<section>
  <h2 class="abs section-title" style="top:1725px">Steps to sell</h2>
  <p class="abs section-sub" style="top:1772px">Nunc finibus purus id erat ultrices, id ultricies urna interdum.</p>

  <div class="abs step" style="left:172px;top:1858px"><h3>1. You fill out your contact details</h3><p>Lorem ipsum dolor sit amet, consectetur adipiscing elit. Donec lobortis nisi vel lectus mattis venenatis. Etiam iaculis volutpat congue. Nam eu faucibus massa. Praesent congue et neque vitae sollicitudin. Pellentesque habitant morbi tristique senectus et netus et malesuada fames vitae,</p></div>
  <div class="abs rule" style="left:172px;top:2005px;width:412px"></div>
  <div class="abs step" style="left:172px;top:2047px"><h3>3. You will receive a non-binding purchase offer</h3><p>Lorem ipsum dolor sit amet, consectetur adipiscing elit. Donec lobortis nisi vel lectus mattis venenatis. Etiam iaculis volutpat congue. Nam eu faucibus massa. Praesent congue et neque vitae sollicitudin. Pellentesque habitant morbi tristique senectus et netus et malesuada fames ac turpis egestas. Donec eget blandit metus. Suspendisse vel orci fermentum, bibendum quam</p></div>

  <div class="abs step" style="left:617px;top:1858px"><h3>2. We will send you a form and a label for shipping<br>(no postage for you!)</h3><p>Lorem ipsum dolor sit amet, consectetur adipiscing elit. Donec lobortis nisi vel lectus mattis venenatis. Etiam iaculis volutpat congue. Nam eu faucibus massa. Praesent congue et neque vitae sollicitudin. Pellentesque habitant morbi tristique senectus et netus et malesuada fames ac turpis egestas. Donec eget blandit metus. Suspendisse vel orci fermentum, bibendum quam</p></div>
  <div class="abs rule" style="left:617px;top:2040px;width:412px"></div>
  <div class="abs step" style="left:617px;top:2083px"><h3>4. You will receive the money transferred</h3><p>Lorem ipsum dolor sit amet, consectetur adipiscing elit. Donec lobortis nisi vel lectus mattis venenatis. Etiam iaculis volutpat congue. Nam eu faucibus massa. Praesent congue et neque vitae sollicitudin. Pellentesque habitant</p></div>
</section>

<section>
  <div class="abs heritage" role="img" aria-label="Darkened close-up of old coins in warm gold tones"></div>
  <p class="abs heritage-text">We have been in the stamp and coin trade<br>for nearly 100 years.</p>
</section>

<footer>
  <div class="abs footer"></div>
  <div class="abs foot-col" style="left:172px"><h4>Kundenservice</h4><ul><li>Vertrauensgarantie</li><li>Versand</li></ul></div>
  <div class="abs foot-col" style="left:385px"><h4>Kontakt</h4><ul><li>Kontakt</li><li>Impressum</li></ul></div>
  <div class="abs foot-col" style="left:597px"><h4>Information</h4><ul><li>AGB</li><li>Widerruf</li><li>Datenschutz</li></ul></div>
  <div class="abs foot-call">Call 0445550000</div>
  <div class="abs foot-mail">Email : info@briefhaus-tanner.ch</div>
  <div class="abs social"><span class="square"></span><span><b>Like Us</b><br>on Plaudernetz</span></div>
  <div class="abs bottom-bar">Copyrights © 2014 All Rights Reserved by Northfold Studio<br>Terms of Use / Privacy Policy</div>
</footer>

</body>
</html>
```